Flyer for Harbourline Accounting & Taxation, a local tax practice

Flyer for my business to be distributed locally in the Western Suburb of Melbourne (Size: DL, Fold: Flat, Backside: Blank) This will include below information (Font, color and capitalization of the text is for the designer's creativity):
Harbourline Accounting & Taxation Your Local Tax Accountant
ABN: 37 481 259 604
Address: 9 Marlo Place, Wattle Bend
kolvend@hbatx.com.au
Call Tobias on 0419 786 205 to book your appointment
Services we offer:
Individual & Company Tax Returns
Company & Trust formation
Business Advisory
Bookkeeping
BAS & IAS
Payroll
TPAR
Please include the logo of the business attached which was designed by PixelForum few years ago.
Please include the NBF, RCQ and Lumo logos somewhere in the bottom, preferable the same size and aligned (attached)

```html
<!DOCTYPE html>
<html lang="en">
<head>
<meta charset="utf-8">
<title>Harbourline Accounting &amp; Taxation – Flyer</title>
<link href="https://fonts.googleapis.com/css2?family=Montserrat:wght@400;600;700;800&family=Anton&display=swap" rel="stylesheet">
<style>
  :root{
    --bg:#c4c8ca;
    --paper:#ffffff;
    --orange:#ec7a35;
    --orange-deep:#e2601e;
    --blue:#1f8fc2;
    --navy-blue:#0f6aa6;
    --charcoal:#4a4b4d;
    --ink:#1d1d1f;
    --muted:#6b6f73;
    --photo-a:#dfe7ee;
    --photo-b:#8aa2b8;
    --photo-c:#f1f1f1;
    --photo-d:#9a9c9f;
  }
  *{box-sizing:border-box;margin:0;padding:0}
  html,body{width:1200px;height:1200px;overflow:hidden}
  body{background:var(--bg);font-family:'Montserrat',sans-serif;color:var(--ink);position:relative}

  .spread{position:absolute;left:60px;top:140px;width:1080px;height:920px;display:flex;box-shadow:0 20px 50px rgba(0,0,0,.18)}
  .panel{position:relative;width:540px;height:920px;background:var(--paper);overflow:hidden}

  /* ---------- front panel ---------- */
  .brand{position:absolute;left:34px;top:30px;display:flex;align-items:center;gap:14px;z-index:2}
  .brand-square{width:46px;height:46px;background:var(--charcoal)}
  .brand-name{font-weight:700;font-size:30px;letter-spacing:3px;color:var(--orange);line-height:1}
  .brand-sub{font-weight:400;font-size:16px;color:var(--charcoal);margin-top:4px;letter-spacing:.5px}

  .photo-meeting{position:absolute;left:0;top:100px;width:540px;height:330px;
    background:linear-gradient(160deg,var(--photo-c) 0%,var(--photo-a) 35%,var(--photo-b) 100%)}

  .services-head{position:absolute;left:0;top:430px;width:540px;height:58px;background:var(--blue);
    color:#fff;font-weight:700;font-size:30px;padding:10px 30px}
  .services-body{position:absolute;left:0;top:488px;width:540px;height:262px;background:var(--orange);padding:18px 30px}
  .service-list{list-style:none}
  .service-list li{display:flex;align-items:flex-start;gap:12px;color:#fff;font-weight:700;font-size:20px;line-height:1.14;margin-bottom:6px}
  .service-list svg{flex:none;margin-top:2px}

  .trusted{position:absolute;left:0;top:750px;width:540px;height:44px;background:var(--charcoal);
    color:#fff;font-weight:800;font-size:20px;letter-spacing:1px;text-align:right;padding:10px 30px}

  .affiliations{position:absolute;left:0;top:794px;width:540px;height:112px;display:flex;align-items:center;justify-content:space-around;padding:0 24px}
  .affil{display:flex;align-items:center;gap:8px}
  .affil-dot{width:34px;height:34px;border-radius:50%;background:var(--blue)}
  .affil-name{font-weight:700;font-size:20px;color:var(--navy-blue)}
  .affil-badge{width:62px;height:62px;border-radius:50%;border:3px solid #8cc63f;background:#fff}
  .affil-partner{width:58px;height:58px;border-radius:50%;background:var(--navy-blue)}
  .foot-strip{position:absolute;left:0;bottom:0;width:540px;height:14px;background:var(--orange)}

  /* ---------- inside panel ---------- */
  .photo-desk{position:absolute;left:0;top:0;width:540px;height:340px;
    background:linear-gradient(180deg,var(--photo-d) 0%,var(--photo-c) 70%,#fff 100%)}
  .headline{position:absolute;left:40px;top:190px;font-family:'Anton',sans-serif;font-size:38px;line-height:1.02;text-transform:none}
  .headline .dark{color:var(--ink)}
  .headline .accent{color:var(--orange-deep)}
  .tagline{display:inline-block;margin-top:6px;background:var(--orange-deep);color:#fff;font-family:'Anton',sans-serif;font-size:22px;padding:3px 12px;letter-spacing:.5px}

  .about{position:absolute;left:40px;top:370px;width:460px}
  .section-title{font-weight:700;font-size:28px;color:var(--navy-blue);line-height:1.1}
  .section-title.small{font-size:24px;margin-top:14px}
  .copy{font-size:13px;font-weight:600;line-height:1.35;text-align:justify;color:var(--ink)}

  .details{position:absolute;left:40px;top:640px;width:470px;color:var(--navy-blue)}
  .abn{font-weight:700;font-size:22px}
  .detail-line{font-weight:600;font-size:16px;margin-top:4px}

  .call-band{position:absolute;left:0;bottom:0;width:540px;height:150px;background:var(--navy-blue);color:#fff;padding:22px 36px}
  .call-lead{font-weight:600;font-size:22px}
  .call-row{display:flex;align-items:center;gap:14px}
  .call-number{font-weight:800;font-size:52px;line-height:1.05;letter-spacing:1px}
  .call-tail{font-weight:600;font-size:17px;text-align:right}
</style>
</head>
<body>
  <div class="spread">
    <!-- Front panel -->
    <section class="panel panel-front">
      <div class="brand">
        <div class="brand-square"></div>
        <div>
          <div class="brand-name">HARBOURLINE</div>
          <div class="brand-sub">Accounting &amp; Taxation</div>
        </div>
      </div>

      <div class="photo-meeting" role="img" aria-label="Photo of business people shaking hands across a meeting table"></div>

      <div class="services-head">Services we offer:</div>
      <div class="services-body">
        <ul class="service-list">
          <li><svg width="22" height="22" viewBox="0 0 22 22"><rect x="1" y="3" width="16" height="16" fill="none" stroke="#fff" stroke-width="2"/><path d="M5 11l4 4 11-13" fill="none" stroke="#fff" stroke-width="3"/></svg>Individual &amp; Company Tax Returns</li>
          <li><svg width="22" height="22" viewBox="0 0 22 22"><rect x="1" y="3" width="16" height="16" fill="none" stroke="#fff" stroke-width="2"/><path d="M5 11l4 4 11-13" fill="none" stroke="#fff" stroke-width="3"/></svg>Company &amp; Trust formation</li>
          <li><svg width="22" height="22" viewBox="0 0 22 22"><rect x="1" y="3" width="16" height="16" fill="none" stroke="#fff" stroke-width="2"/><path d="M5 11l4 4 11-13" fill="none" stroke="#fff" stroke-width="3"/></svg>Business Advisory</li>
          <li><svg width="22" height="22" viewBox="0 0 22 22"><rect x="1" y="3" width="16" height="16" fill="none" stroke="#fff" stroke-width="2"/><path d="M5 11l4 4 11-13" fill="none" stroke="#fff" stroke-width="3"/></svg>bookKeeping</li>
          <li><svg width="22" height="22" viewBox="0 0 22 22"><rect x="1" y="3" width="16" height="16" fill="none" stroke="#fff" stroke-width="2"/><path d="M5 11l4 4 11-13" fill="none" stroke="#fff" stroke-width="3"/></svg>BAS &amp; IAS</li>
          <li><svg width="22" height="22" viewBox="0 0 22 22"><rect x="1" y="3" width="16" height="16" fill="none" stroke="#fff" stroke-width="2"/><path d="M5 11l4 4 11-13" fill="none" stroke="#fff" stroke-width="3"/></svg>Payrolls</li>
          <li><svg width="22" height="22" viewBox="0 0 22 22"><rect x="1" y="3" width="16" height="16" fill="none" stroke="#fff" stroke-width="2"/><path d="M5 11l4 4 11-13" fill="none" stroke="#fff" stroke-width="3"/></svg>TPAR</li>
        </ul>
      </div>

      <div class="trusted">TRUSTED FIRM</div>

      <div class="affiliations">
        <div class="affil"><span class="affil-dot"></span><span class="affil-name">NBF</span></div>
        <div class="affil"><span class="affil-badge"></span></div>
        <div class="affil"><span class="affil-name">Lumo</span><span class="affil-partner"></span></div>
      </div>
      <div class="foot-strip"></div>
    </section>

    <!-- Inside panel -->
    <section class="panel panel-inside">
      <div class="photo-desk" role="img" aria-label="Photo of hands pointing a pen at financial charts beside a laptop"></div>

      <div class="headline">
        <div class="dark">Harbourline</div>
        <div class="accent">Accounting</div>
        <div><span class="dark">and</span> <span class="accent">Taxation</span></div>
        <div class="tagline">Your Local Tax Accountant</div>
      </div>

      <div class="about">
        <h2 class="section-title">ABOUT US</h2>
        <p class="copy">Lorem ipsum dolor sit amet, consectetur adipiscing elit, sed do eiusmod tempor incididunt ut labore et dolore magna aliqua. Quis ipsum suspendisse ultrices gravida. Risus commodo viverra maecenas accumsan lacus vel facilisis.</p>
        <h3 class="section-title small">Bookeeping</h3>
        <p class="copy">Lorem ipsum dolor sit amet, consectetur adipiscing elit, sed do eiusmod tempor incididunt ut labore et dolore magna aliqua.</p>
      </div>

      <div class="details">
        <div class="abn">ABN: 37 481 259 604</div>
        <div class="detail-line">Address: 9 Marlo Place, Wattle Bend</div>
        <div class="detail-line">kolvend@hbatx.com.au</div>
      </div>

      <div class="call-band">
        <div class="call-lead">Call Tobias on</div>
        <div class="call-row">
          <svg width="44" height="44" viewBox="0 0 24 24" aria-hidden="true"><path fill="#fff" d="M6.6 10.8a15.1 15.1 0 006.6 6.6l2.2-2.2c.3-.3.7-.4 1-.2 1.1.4 2.3.6 3.6.6.6 0 1 .4 1 1V20c0 .6-.4 1-1 1A17 17 0 013 4c0-.6.4-1 1-1h3.5c.6 0 1 .4 1 1 0 1.3.2 2.5.6 3.6.1.3 0 .7-.2 1z"/></svg>
          <div class="call-number">0419 786 205</div>
        </div>
        <div class="call-tail">to book your appointment</div>
      </div>
    </section>
  </div>
</body>
</html>
```